Christian Camp Meetings Website Design

**Do not contact me privately; all inquiries will be ignored.**

Industry: Nonprofit Christian camp meetings for children, youth, and adults.

Target Market: Families and individuals seeking a faith-based camp experience.

Description:
This website should provide a visually appealing and easy-to-navigate platform that clearly highlights how visitors can register for camp events and make donations. A straightforward design will make it simple for users to access registration forms, donation buttons, and key event & camp details.

Look and Feel:
• Clean, user-friendly layout focused on clarity and accessibility.
• Primarily blue tones to evoke a calm and welcoming atmosphere.
• Clear, readable Google fonts only.
• If using images only use royalty-free stock photos showcasing participants at camp activities, encouraging new registrations and donations.

Pages to Create:
1. Main Page: A welcoming overview that prominently features call-to-action buttons for registration and donations.
2. Christian Camp Meetings Page: Detailed event information with links to registration forms and suggested donation amounts.
3. Youth Program Page: Descriptions of youth events, programs, and an easy-to-find registration link.
4. Children’s Camp Page: Information about the children’s Bible camp, with a focus on how parents can register their kids.
5. History Page: A brief look at the organization’s origins, with an integrated “Donate Now” button to support ongoing programs.

Examples of Desired Style:
• https://www.brightharborfellowship.org/nrv/
• https://walkingopenroad.com/
• https://www.pinemeadowchapel.org/
• https://kv.church/

Content Source:
Use content from the link provided in the attachment here as the primary source for all textual and media content.

Important Notes:
• Do not contact me privately; all inquiries will be ignored.
• The website should emphasize registration and donations as key actions.
• Avoid overlapping elements in the design; maintain a clean and structured layout.
• Ensure that only Google fonts and royalty-free stock photos are used.

Target Market(s)

Christian families looking for events

Industry/Entity Type

Christian faith based camp

Number of Pages Required

5+ page

Colors
0094D4
00A9DD
6FCCEA
C7EBF8
E9F6FB

Requirements
Should not have
• No search bar, limited or no overlapping elements

```html
<!DOCTYPE html>
<html lang="en">
<head>
<meta charset="utf-8">
<title>Children's Camp – Cedar Hollow Holiness Camp</title>
<link rel="stylesheet" href="https://fonts.googleapis.com/css2?family=Poppins:wght@400;500;600&family=Lora:wght@400;500&display=swap">
<style>
:root{
  --blue:#0094d4;
  --blue-bright:#00a9dd;
  --blue-soft:#6fccea;
  --blue-pale:#c7ebf8;
  --blue-mist:#e9f6fb;
  --navy:#1f6d9a;
  --green:#7aa85a;
  --ink:#2b2b2b;
  --muted:#5c5c5c;
  --footer:#2b2e33;
  --white:#ffffff;
}
*{box-sizing:border-box;margin:0;padding:0}
html,body{width:699px;height:1200px;overflow:hidden;background:var(--white)}
body{font-family:"Poppins",sans-serif;color:var(--ink);position:relative}
.serif{font-family:"Lora",serif}

.site-header{height:68px;display:flex;align-items:center;justify-content:space-between;padding:0 66px 0 60px}
.brand{display:flex;align-items:center;gap:6px}
.brand-mark{width:14px;height:14px;border-radius:50%;background:var(--blue-soft)}
.brand-name{font-size:9px;font-weight:600;color:var(--navy);line-height:1.2;width:80px}
.header-actions{display:flex;gap:10px;margin-top:-22px}
.btn{display:inline-flex;align-items:center;justify-content:center;gap:5px;color:var(--white);font-size:8px;font-weight:500;border-radius:3px;text-decoration:none}
.btn-green{background:var(--green)}
.btn-blue{background:var(--blue)}
.header-actions .btn{width:74px;height:22px}

.main-nav{height:26px;background:var(--blue);display:flex;justify-content:center}
.main-nav a{color:var(--white);font-size:7px;text-decoration:none;padding:0 16px;display:flex;align-items:center}
.main-nav a.active{background:var(--navy)}
.main-nav a.contact{background:var(--green);margin-left:8px;padding:0 20px}

.hero{position:relative;height:176px}
.hero-photo{position:absolute;inset:0;background:linear-gradient(180deg,#5b8aa6 0%,#7ea9c2 45%,#a9c6d6 75%,#ffffff 100%)}
.hero h1{position:absolute;top:78px;width:100%;text-align:center;color:var(--white);font-size:30px;font-weight:400}

.intro{padding:46px 0 0 112px;width:600px}
.intro h2{font-size:15.5px;font-weight:500;color:var(--navy);margin-bottom:10px}
.intro p{font-size:7.5px;line-height:1.6;color:var(--muted);width:470px}
.expect{margin-top:22px}
.expect h3{font-size:15px;font-weight:500;color:var(--navy);margin-bottom:8px}
.expect ul{list-style:none}
.expect li{font-size:7.5px;color:var(--muted);line-height:1.75;display:flex;align-items:center;gap:5px}
.expect li b{font-weight:400;color:var(--blue)}

.events{margin-top:44px;text-align:center}
.events h2{font-size:20px;font-weight:400;color:var(--navy);margin-bottom:20px}
.event-grid{display:flex;justify-content:center;gap:14px}
.event-card{width:124px;text-align:center}
.event-photo{height:86px;border-radius:2px}
.event-card h4{font-size:10px;font-weight:400;color:var(--navy);margin:10px 0 4px}
.event-card p{font-size:5.5px;color:var(--muted);line-height:1.5}
.event-card .btn{width:50px;height:15px;font-size:5.5px;margin-top:8px}

.give{position:absolute;top:790px;left:0;width:699px;height:175px;background:linear-gradient(180deg,var(--blue-bright),var(--blue));text-align:center;color:var(--white);padding-top:24px}
.give h2{font-size:18px;font-weight:500;line-height:1.25}
.give p{font-size:7.5px;line-height:1.6;width:340px;margin:12px auto 0}
.give .btn{width:116px;height:30px;font-size:8.5px;margin-top:14px}

.site-footer{position:absolute;top:965px;left:0;width:699px;height:235px;background:var(--footer);color:var(--white)}
.footer-badge{position:absolute;left:50%;top:-22px;transform:translateX(-50%);width:68px;height:68px;border-radius:50%;background:var(--white);display:flex;align-items:center;justify-content:center;text-align:center;font-size:6px;font-weight:600;color:var(--navy);line-height:1.25;padding:0 8px}
.footer-contact{position:absolute;left:60px;top:66px}
.footer-contact h5,.footer-news h5{font-size:10px;font-weight:500;margin-bottom:6px}
.footer-contact p{font-size:5.5px;line-height:1.65;color:#d5d7da}
.footer-news{position:absolute;left:252px;top:66px;width:195px;text-align:center}
.footer-news small{display:block;font-size:5.5px;color:#d5d7da;margin-bottom:6px}
.email-field{display:flex;align-items:center;justify-content:space-between;height:24px;background:#3d4147;border-radius:2px;padding:0 8px;font-size:6px;color:#b7bbc0}
.social{display:flex;justify-content:center;gap:10px;margin-top:14px}
.social span{width:9px;height:9px;border-radius:50%;background:#d5d7da}
.footer-actions{position:absolute;right:64px;top:68px;display:flex;flex-direction:column;gap:12px}
.footer-actions .btn{width:108px;height:30px;font-size:8.5px}
.copyright{position:absolute;bottom:10px;width:100%;text-align:center;font-size:5px;color:#9ca0a6}
</style>
</head>
<body>

<header class="site-header">
  <div class="brand">
    <span class="brand-mark"></span>
    <span class="brand-name">CEDAR HOLLOW HOLINESS CAMP</span>
  </div>
  <div class="header-actions">
    <a class="btn btn-green" href="#">
      <svg width="8" height="8" viewBox="0 0 10 10"><path d="M5 9 1.3 5.3A2.2 2.2 0 0 1 5 2.3a2.2 2.2 0 0 1 3.7 3Z" fill="#fff"/></svg>Donate</a>
    <a class="btn btn-blue" href="#">
      <svg width="8" height="8" viewBox="0 0 10 10"><circle cx="5" cy="3" r="2" fill="#fff"/><path d="M1 9.5a4 4 0 0 1 8 0Z" fill="#fff"/></svg>Register</a>
  </div>
</header>

<nav class="main-nav">
  <a href="#">Home</a>
  <a href="#">Camp Meetings</a>
  <a href="#">Youth Programs</a>
  <a href="#" class="active">Children's Camp</a>
  <a href="#">History</a>
  <a href="#" class="contact">Contact Us</a>
</nav>

<section class="hero">
  <div class="hero-photo" role="img" aria-label="Children running and playing outdoors in silhouette against a bright sky"></div>
  <h1 class="serif">Children's Camp</h1>
</section>

<section class="intro">
  <h2>A Safe and Exciting Christian Camp for Children</h2>
  <p>Cedar Hollow Children's Camp is a special place where kids can grow in their faith, make new friends, and enjoy exciting activities in a safe, Christ-centered environment. Our camp is designed to help children learn about God through engaging Bible lessons, worship, and fun outdoor adventures.</p>

  <div class="expect">
    <h3>What to Expect at Children's Camp</h3>
    <ul>
      <li><svg width="7" height="7" viewBox="0 0 10 10"><path d="M1.5 5.2 4 7.6 8.6 2.4" stroke="#0094d4" stroke-width="1.6" fill="none"/></svg><span><b>Daily Bible Lessons &amp; Worship</b> – Teaching kids about God's love in a fun and interactive way.</span></li>
      <li><svg width="7" height="7" viewBox="0 0 10 10"><path d="M1.5 5.2 4 7.6 8.6 2.4" stroke="#0094d4" stroke-width="1.6" fill="none"/></svg><span><b>Exciting Outdoor Activities</b> – Games, sports, crafts, and nature exploration.</span></li>
      <li><svg width="7" height="7" viewBox="0 0 10 10"><path d="M1.5 5.2 4 7.6 8.6 2.4" stroke="#0094d4" stroke-width="1.6" fill="none"/></svg><span><b>New Friendships</b> – A welcoming environment where kids build lasting friendships.</span></li>
      <li><svg width="7" height="7" viewBox="0 0 10 10"><path d="M1.5 5.2 4 7.6 8.6 2.4" stroke="#0094d4" stroke-width="1.6" fill="none"/></svg><span><b>Safe &amp; Supervised Environment</b> – Experienced staff ensuring a safe and nurturing space.</span></li>
    </ul>
  </div>
</section>

<section class="events">
  <h2 class="serif">Upcoming Children's Camp</h2>
  <div class="event-grid">
    <article class="event-card">
      <div class="event-photo" role="img" aria-label="Children gathered around an open Bible" style="background:linear-gradient(135deg,#8a6a52,#c9a98a)"></div>
      <h4 class="serif">Spring Revival Meeting</h4>
      <p>Cedar Hollow Campgrounds<br>Weekends in April</p>
      <a class="btn btn-blue" href="#">Register Now</a>
    </article>
    <article class="event-card">
      <div class="event-photo" role="img" aria-label="Hands joined together in prayer at summer camp" style="background:linear-gradient(135deg,#6f5a4c,#b59b86)"></div>
      <h4 class="serif">Summer Camp Meeting</h4>
      <p>Cedar Hollow Campgrounds<br>Weekends in June</p>
      <a class="btn btn-blue" href="#">Register Now</a>
    </article>
    <article class="event-card">
      <div class="event-photo" role="img" aria-label="Young people raising hands in worship" style="background:linear-gradient(135deg,#4f86a8,#9cc4da)"></div>
      <h4 class="serif">Youth Renewal Weekend</h4>
      <p>Cedar Hollow Campgrounds<br>Weekends in August</p>
      <a class="btn btn-blue" href="#">Register Now</a>
    </article>
  </div>
</section>

<section class="give">
  <h2>Cedar Hollow Camp Association now<br>has online giving.</h2>
  <p>You can sign up for a one-time, weekly, or monthly gift. It is easy to edit the amount or frequency or even cancel if you need to do that.</p>
  <a class="btn btn-green" href="#">
    <svg width="9" height="9" viewBox="0 0 10 10"><path d="M5 9 1.3 5.3A2.2 2.2 0 0 1 5 2.3a2.2 2.2 0 0 1 3.7 3Z" fill="#fff"/></svg>Donate Now</a>
</section>

<footer class="site-footer">
  <div class="footer-badge">CEDAR HOLLOW HOLINESS CAMP</div>
  <div class="footer-contact">
    <h5>Contact</h5>
    <p>Cedar Hollow Holiness Camp<br>1420 Ridge Road<br>Millbrook, OH 44000<br>Phone 555-201-4470 (dining room)<br>Phone 555-201-4482 (office)</p>
  </div>
  <div class="footer-news">
    <h5>Stay Updated</h5>
    <small>Join Our Mailing list</small>
    <div class="email-field"><span>Enter your email</span>
      <svg width="8" height="8" viewBox="0 0 10 10"><path d="M2 5h6M5.5 2.5 8 5 5.5 7.5" stroke="#b7bbc0" stroke-width="1.2" fill="none"/></svg></div>
    <div class="social"><span></span><span></span><span></span></div>
  </div>
  <div class="footer-actions">
    <a class="btn btn-blue" href="#">
      <svg width="9" height="9" viewBox="0 0 10 10"><circle cx="5" cy="3" r="2" fill="#fff"/><path d="M1 9.5a4 4 0 0 1 8 0Z" fill="#fff"/></svg>Register Now</a>
    <a class="btn btn-green" href="#">
      <svg width="9" height="9" viewBox="0 0 10 10"><path d="M5 9 1.3 5.3A2.2 2.2 0 0 1 5 2.3a2.2 2.2 0 0 1 3.7 3Z" fill="#fff"/></svg>Donate Now</a>
  </div>
  <p class="copyright">© 2025 Cedar Hollow Holiness Camp. All Rights Reserved.</p>
</footer>

</body>
</html>
```